New business stationairy

I need paper with header and footer and business cards.
I am a Ltd Company and my main field of expertise is QA/QC inspection in the Oil and Gas Industry. I will need all contact detail inserted and a footer with registration number and bank details etc

Industry/Entity Type

Business

```html
<!DOCTYPE html>
<html lang="en">
<head>
<meta charset="utf-8">
<title>Halden Inspection Services Ltd – Letterhead</title>
<link href="https://fonts.googleapis.com/css2?family=Open+Sans:wght@400;600;700&display=swap" rel="stylesheet">
<style>
  :root {
    --navy: #1b1f4b;
    --grey: #8d8f94;
    --grey-light: #b5b7bb;
    --paper: #ffffff;
    --ink: #3a3c44;
  }
  * { margin: 0; padding: 0; box-sizing: border-box; }
  html, body { width: 874px; height: 1200px; overflow: hidden; background: var(--paper); }
  .letterhead {
    position: relative;
    width: 874px;
    height: 1200px;
    background: var(--paper);
    font-family: "Open Sans", Arial, sans-serif;
    color: var(--ink);
  }
  .header-shapes, .footer-shapes { position: absolute; left: 0; width: 874px; }
  .header-shapes { top: 0; height: 180px; }
  .footer-shapes { top: 1030px; height: 50px; }

  .company-name {
    position: absolute;
    left: 64px;
    top: 34px;
    font-family: "Open Sans", Arial, sans-serif;
    font-weight: 600;
    font-size: 44px;
    line-height: 48px;
    text-transform: uppercase;
    color: var(--navy);
  }

  .contact-bar {
    position: absolute;
    left: 66px;
    top: 141px;
    display: flex;
    gap: 44px;
    font-family: "Open Sans", Arial, sans-serif;
    font-weight: 700;
    font-size: 14px;
    line-height: 18px;
    color: #fff;
  }
  .contact-item { display: flex; align-items: center; gap: 8px; }
  .contact-item svg { width: 13px; height: 13px; fill: #fff; }

  .address {
    position: absolute;
    left: 70px;
    top: 186px;
    font-size: 13px;
    line-height: 19px;
    font-style: normal;
  }
  .address-label {
    font-weight: 700;
    color: var(--navy);
    font-size: 13px;
  }

  .registration {
    position: absolute;
    left: 345px;
    top: 1035px;
    font-size: 14px;
    line-height: 18px;
    color: var(--navy);
  }
  .registration strong { font-weight: 700; }
  .bank-info {
    position: absolute;
    left: 345px;
    top: 1084px;
    font-size: 14px;
    color: var(--navy);
  }
</style>
</head>
<body>
<main class="letterhead">
  <svg class="header-shapes" viewBox="0 0 874 180" aria-hidden="true">
    <polygon points="0,0 590,0 560,24 0,24" fill="var(--navy)"/>
    <polygon points="0,136 600,136 584,164 0,164" fill="var(--grey)"/>
  </svg>

  <h1 class="company-name">Halden Inspection<br>Services Ltd</h1>

  <div class="contact-bar">
    <span class="contact-item">
      <svg viewBox="0 0 24 24"><path d="M6.6 10.8a15.1 15.1 0 0 0 6.6 6.6l2.2-2.2a1 1 0 0 1 1-.25 11.4 11.4 0 0 0 3.6.57 1 1 0 0 1 1 1V20a1 1 0 0 1-1 1A17 17 0 0 1 3 4a1 1 0 0 1 1-1h3.5a1 1 0 0 1 1 1c0 1.25.2 2.45.57 3.57a1 1 0 0 1-.25 1z"/></svg>
      07700 900418
    </span>
    <span class="contact-item">
      <svg viewBox="0 0 24 24"><path d="M2 5h20v14H2z M3.5 6.5 12 13l8.5-6.5" fill="#fff" stroke="var(--grey)" stroke-width="1.5"/></svg>
      office@haldeninspect.co.uk
    </span>
  </div>

  <address class="address">
    <div class="address-label">ADDRESS:</div>
    The Willows<br>
    Mill Lane<br>
    Ashby<br>
    Marden Vale<br>
    Wessex<br>
    WX4 7PL
  </address>

  <svg class="footer-shapes" viewBox="0 0 874 50" aria-hidden="true">
    <polygon points="310,0 874,0 874,26 326,26" fill="var(--grey-light)"/>
  </svg>

  <p class="registration">Company Registration <strong># 4410286</strong></p>
  <p class="bank-info">Bank Information:</p>
</main>
</body>
</html>
```